Tallow Crest Business Card

We need a business card designed for a a company called "Tallow Crest". We offer consulting, coaching and training to business leaders and coaches (across the world) using the latest findings in neuroscience, social and emotional intelligence and positive psychology. The final design should communicate the use of brain science to create sustainable relationships.

The card should be doublesided. The logo is attached and names and titles will be provided to the successful designer. Thank you.

Industry/Entity Type

Training

```html
<!DOCTYPE html>
<html lang="en">
<head>
<meta charset="utf-8">
<title>Tallow Crest Business Card</title>
<link rel="stylesheet" href="https://fonts.googleapis.com/css2?family=Source+Sans+3:wght@400;700&display=swap">
<style>
  :root {
    --ink: #111111;
    --paper: #ffffff;
    --brand-blue: #008fc5;
    --brand-green: #c2d92e;
    --charcoal: #231f20;
    --frame-grey: #b5b5b5;
    --text-font: "Source Sans 3", "Myriad Pro", Arial, sans-serif;
  }
  * { box-sizing: border-box; margin: 0; padding: 0; }
  html, body { width: 1200px; height: 1000px; overflow: hidden; background: var(--paper); }
  body { position: relative; font-family: var(--text-font); color: var(--ink); }

  .card { position: absolute; }
  .card--front { left: 34px; top: 220px; width: 319px; height: 554px; border: 2px solid var(--frame-grey); background: var(--paper); }
  .card--charcoal { left: 371px; top: 224px; width: 314px; height: 550px; background: var(--charcoal); }
  .card--blue { left: 729px; top: 223px; width: 197px; height: 346px; background: var(--brand-blue); }
  .card--green { left: 962px; top: 224px; width: 197px; height: 346px; background: var(--brand-green); }

  .brand { position: absolute; left: 0; right: 0; display: flex; align-items: center; justify-content: center; gap: 10px; font-weight: 700; white-space: nowrap; }
  .brand__square { display: block; flex: none; }
  .card--front .brand { top: 300px; color: var(--brand-blue); font-size: 34px; }
  .card--front .brand__square { width: 30px; height: 30px; background: var(--brand-green); }
  .card--charcoal .brand { top: 440px; color: var(--paper); font-size: 36px; }
  .card--charcoal .brand__square { width: 30px; height: 30px; background: var(--paper); }
  .card--blue .brand, .card--green .brand { top: 380px; color: var(--paper); font-size: 22px; gap: 7px; }
  .card--blue .brand__square, .card--green .brand__square { width: 18px; height: 18px; background: var(--paper); }

  .contact { position: absolute; left: 0; right: 0; text-align: center; }
  .contact__name { top: 308px; font-size: 23px; letter-spacing: 0.2px; }
  .contact__role { top: 335px; font-size: 15px; color: var(--brand-green); }
  .contact__email { top: 375px; font-size: 22px; }
  .contact__phone { top: 405px; font-size: 22px; }
  .card__rule { position: absolute; left: 1px; right: 1px; top: 478px; height: 2px; background: var(--brand-green); }
  .address { position: absolute; left: 66px; top: 494px; font-size: 15.5px; line-height: 21px; }

  .web { position: absolute; left: 0; right: 0; text-align: center; color: var(--paper); }
  .card--charcoal .web { top: 371px; font-size: 16.5px; }
  .card--blue .web, .card--green .web { top: 232px; font-size: 10.5px; }

  .caption { position: absolute; font-size: 25px; text-align: center; white-space: nowrap; transform: translateX(-50%); }
  .caption--front { left: 188px; top: 799px; }
  .caption--back1 { left: 524px; top: 809px; }
  .caption--back2 { left: 831px; top: 598px; }
  .caption--back3 { left: 1060px; top: 598px; }
</style>
</head>
<body>
  <section class="card card--front" aria-label="Card front">
    <div class="brand" style="top:70px;"><span class="brand__square"></span>Tallow Crest</div>
    <p class="contact contact__name">MARA LINDQVIST</p>
    <p class="contact contact__role">position</p>
    <p class="contact contact__email">mara@tallowcrest.com</p>
    <p class="contact contact__phone">555.204.7316</p>
    <div class="card__rule"></div>
    <p class="address">417 Harbor Bend Road<br>Larkspur, OR 97411-2208</p>
  </section>
  <p class="caption caption--front">front design</p>

  <section class="card card--charcoal" aria-label="Card back, charcoal">
    <div class="brand" style="top:258px;"><span class="brand__square"></span>Tallow Crest</div>
    <p class="web">www.tallowcrest.com</p>
  </section>
  <p class="caption caption--back1">back design #1</p>

  <section class="card card--blue" aria-label="Card back, blue">
    <div class="brand" style="top:160px;"><span class="brand__square"></span>Tallow Crest</div>
    <p class="web">www.tallowcrest.com</p>
  </section>
  <p class="caption caption--back2">back design #2</p>

  <section class="card card--green" aria-label="Card back, green">
    <div class="brand" style="top:160px;"><span class="brand__square"></span>Tallow Crest</div>
    <p class="web">www.tallowcrest.com</p>
  </section>
  <p class="caption caption--back3">back design #3</p>
</body>
</html>
```